Sol Bocado Digital Menu Boards

IF SELECTED, WINNER MAY BE HIRED FOR OTHER DESIGNS OF DIFFERENT STORES OF OUR COMPANY.

Task: Digital Menu Boards Design

Task description: We need designs for a Digital Menu to be displayed on two 42’’screens at Solbocado, a fast-food restaurant in Guadalajara, Mexico. The menu redesign should communicate to our customers the experience of eating at our restaurant.

For avoiding the creation of videos, we are expecting several menu slides with the same text but with different images, simulating the effect of a video where the images are changing. This menu slides will be projected through a USB memory and a slideshow.

Attached files:
For the design, there are several documents attached to the task description:
1. Logo of the restaurant
2. Pictures of the restaurant
3. Example video of what we want to achieve through this menu slides.
4. Pictures of the actual menu board, to be replaced with the new designs.
5. Menu description (regular and breakfast menu)
6. Pictures of each element on the menu (We don’t have yet any breakfast pictures)
**The files are organized on a ZIP file.

Expected product:
For the regular menu,
• 2 menu slide designs for TACOS Y ESPECIALIDADES, where the text will be exactly the same but the images would differ.
• 2 menu slide designs for BEBIDAS Y EXTRAS, where the text will be exactly the same but the images would differ.
For the breakfast menu,
• 1 menu slide including all the menu
Total: 5 menu board slides.

Technical specs:
• You should send the editable file, med and high resolution JPGs for each design.
• The designs should fit perfectly on 42’’ screens.

Reason: Designers, For the final decision we are asking for a minimum of designs for chosing, we are going to wait a little bit more. Solbocado

Industry/Entity Type

Restaurant

```html
<!DOCTYPE html>
<html lang="es">
<head>
<meta charset="utf-8">
<title>Sol Bocado – Menú Digital</title>
<link rel="stylesheet" href="https://fonts.googleapis.com/css2?family=Lobster&family=Montserrat:wght@500;700&display=swap">
<style>
  :root{
    --page-bg:#e2e2e2;
    --board-red:#cf1f2d;
    --stripe-red:#b91927;
    --panel-white:#ffffff;
    --heading-red:#d22330;
    --text-gray:#555555;
    --logo-cream:#f7d08f;
  }
  *{margin:0;padding:0;box-sizing:border-box}
  html,body{width:1200px;height:1000px;overflow:hidden;background:var(--page-bg)}
  body{position:relative;font-family:"Montserrat",Arial,sans-serif;color:var(--text-gray)}

  .menu-board{
    position:absolute;left:47px;top:149px;width:1107px;height:704px;overflow:hidden;
    background:repeating-linear-gradient(to bottom,var(--board-red) 0 6px,var(--stripe-red) 6px 9px);
  }
  .circle{position:absolute;border-radius:50%;background:var(--panel-white)}
  .circle--photo{left:-22px;top:-154px;width:530px;height:530px;overflow:hidden}
  .photo-fill{
    position:absolute;inset:0;
    background:radial-gradient(circle at 45% 70%,#c8552e 0%,#e4c79a 35%,#f3ecd9 60%,#ffffff 80%),#fff;
  }
  .circle--tacos{left:206px;top:266px;width:500px;height:500px}
  .circle--breakfast{left:553px;top:53px;width:346px;height:346px}
  .circle--drinks{left:778px;top:341px;width:350px;height:350px}

  .section-title{font-family:"Lobster",cursive;color:var(--heading-red);font-weight:400}
  .item-name{font-weight:700;color:var(--heading-red);font-size:14.5px;letter-spacing:.3px}
  .item-price{font-weight:500;font-size:15px;letter-spacing:.4px}
  .item-price .sep{color:var(--heading-red);font-weight:700;margin:0 6px}
  .item-note{font-size:8.5px;font-weight:500;letter-spacing:.2px}

  .menu-tacos{position:absolute;left:256px;top:352px;width:400px;text-align:center}
  .menu-tacos .section-title{font-size:25px;margin-bottom:18px}
  .menu-tacos .menu-item{height:68px}
  .menu-tacos .item-name{line-height:18px}
  .menu-tacos .item-price{line-height:24px}

  .menu-breakfast{position:absolute;left:576px;top:117px;width:300px;text-align:center}
  .menu-breakfast .section-title{font-size:24px;margin-bottom:20px}
  .menu-breakfast .menu-item{height:52px}
  .menu-breakfast .item-name{line-height:18px}
  .menu-breakfast .item-price{line-height:24px}

  .menu-drinks{position:absolute;left:840px;top:414px;width:235px}
  .menu-drinks .item-name{text-align:center;line-height:20px;margin-bottom:12px}
  .price-row{display:flex;justify-content:space-between;align-items:flex-end;font-size:14.5px;font-weight:500;line-height:17px;margin-bottom:4px;letter-spacing:.3px}
  .menu-drinks .extras{margin-top:12px}

  .brand{position:absolute;left:905px;top:28px;width:180px;height:180px}
  .brand-dot{position:absolute;left:45px;top:0;width:90px;height:90px;border-radius:50%;background:var(--logo-cream)}
  .brand-name{position:absolute;left:0;top:98px;width:180px;text-align:center;font-family:"Lobster",cursive;font-size:38px;color:var(--panel-white);line-height:44px}
</style>
</head>
<body>
<main class="menu-board">
  <div class="circle circle--photo">
    <div class="photo-fill" role="img" aria-label="Fotografía de tacos al pastor con cebolla, cilantro, piña, limones, guacamole y pico de gallo"></div>
  </div>
  <div class="circle circle--tacos"></div>
  <div class="circle circle--breakfast"></div>
  <div class="circle circle--drinks"></div>

  <section class="menu-tacos">
    <h2 class="section-title">Tacos y Especialidades</h2>
    <div class="menu-item"><p class="item-name">TACOS</p><p class="item-price">ARRACHERA: $16<span class="sep">I</span>PASTOR: $14</p><p class="item-note">*TORTILLA DE HARINA: + $1</p></div>
    <div class="menu-item"><p class="item-name">QUESADILLA</p><p class="item-price">ARRACHERA: $20<span class="sep">I</span>PASTOR: $18</p><p class="item-note">*TORTILLA DE HARINA: + $1</p></div>
    <div class="menu-item"><p class="item-name">VOLCÁN</p><p class="item-price">ARRACHERA: $20<span class="sep">I</span>PASTOR: $18</p><p class="item-note">*TORTILLA DE HARINA: + $1</p></div>
    <div class="menu-item"><p class="item-name">GRINGA</p><p class="item-price">ARRACHERA: $20<span class="sep">I</span>PASTOR: $18</p><p class="item-note">*TORTILLA DE HARINA: + $2</p></div>
  </section>

  <section class="menu-breakfast">
    <h2 class="section-title">Desayunos</h2>
    <div class="menu-item"><p class="item-name">CHILAQUILES</p><p class="item-price">ARRACHERA: $50<span class="sep">I</span>PASTOR: $45</p></div>
    <div class="menu-item"><p class="item-name">BURRITOS</p><p class="item-price">ARRACHERA: $20<span class="sep">I</span>PASTOR: $18</p></div>
    <div class="menu-item"><p class="item-name">TACOS DORADOS</p><p class="item-price">ARRACHERA: $40<span class="sep">I</span>PASTOR: $45</p></div>
  </section>

  <section class="menu-drinks">
    <h2 class="item-name">BEBIDAS</h2>
    <div class="price-row"><span>CERVEZA NACIONAL</span><span>$ 30</span></div>
    <div class="price-row"><span>CERVEZA IMPORTADA</span><span>$ 40</span></div>
    <div class="price-row"><span>AGUA EMBOTELLADA<br>/REFRESCO</span><span>$ 60</span></div>
    <h2 class="item-name extras">EXTRAS</h2>
    <div class="price-row"><span>GUACAMOLE</span><span>$ 20</span></div>
    <div class="price-row"><span>POSTRE</span><span>$ 15</span></div>
  </section>

  <div class="brand">
    <div class="brand-dot"></div>
    <p class="brand-name">Sol Bocado</p>
  </div>
</main>
</body>
</html>
```